Yoga and Wellness Center

New business- have the logo already, but wanted my cards to be more colorful.

Please find my attached logo. I am only waiting on confirmation of my
telephone number in order to have all the information right. This is for a
new yoga and wellness center in TN for a conservative audience, but I would
like a colorful business card.

Industry/Entity Type

Conservative

```html
<!DOCTYPE html>
<html lang="en">
<head>
<meta charset="utf-8">
<title>Laurel Hollow Yoga – Business Cards</title>
<link href="https://fonts.googleapis.com/css2?family=Open+Sans:ital,wght@0,400;0,600;0,700;1,400;1,700&display=swap" rel="stylesheet">
<style>
  :root {
    --navy: #24337f;
    --orange: #f26a21;
    --paper: #ffffff;
    --paper-shade: #f1f1f3;
    --backdrop: #e6e7ea;
    --ink-light: #ffffff;
  }
  * { box-sizing: border-box; margin: 0; padding: 0; }
  html, body {
    width: 1200px; height: 901px; overflow: hidden;
    background: var(--backdrop);
    font-family: "Open Sans", Arial, sans-serif;
  }
  .sheet {
    width: 1200px; height: 901px;
    display: flex; align-items: center; justify-content: center; gap: 48px;
  }
  .card {
    position: relative;
    width: 520px; height: 297px;
    border-radius: 26px;
    overflow: hidden;
    background: linear-gradient(135deg, var(--paper), var(--paper-shade));
    box-shadow: 0 14px 30px rgba(0,0,0,.18);
  }
  .card-art { position: absolute; inset: 0; width: 100%; height: 100%; }
  .band { fill: var(--navy); }
  .swoosh { fill: var(--orange); }

  .brand {
    position: absolute;
    display: flex; align-items: center; gap: 12px;
    color: var(--navy);
    font-weight: 700;
    font-size: 22px;
    letter-spacing: 3px;
    text-transform: uppercase;
    line-height: 1;
    white-space: nowrap;
  }
  .brand-dot {
    width: 40px; height: 40px; border-radius: 50%;
    background: var(--orange); flex: none;
  }

  /* front */
  .front .brand {
    left: 110px; top: 118px;
    font-size: 17px; letter-spacing: 2px;
  }
  .front .brand-dot { width: 36px; height: 36px; }
  .person {
    position: absolute; left: 24px; top: 16px;
    color: var(--ink-light);
  }
  .person-name { font-size: 19px; font-weight: 700; font-style: italic; line-height: 1.3; }
  .person-role { font-size: 13px; font-style: italic; line-height: 1.3; margin-top: 2px; }
  .contact {
    position: absolute; right: 24px; bottom: 6px;
    list-style: none;
    color: var(--ink-light);
    font-size: 10px; line-height: 1.4;
    text-align: right;
    white-space: nowrap;
  }
  .contact li { display: flex; align-items: center; justify-content: flex-end; gap: 7px; }
  .contact svg { width: 10px; height: 10px; fill: var(--ink-light); flex: none; }

  /* back */
  .back .brand { left: 150px; top: 96px; }
  .web {
    position: absolute; left: 28px; bottom: 26px;
    color: var(--ink-light);
    font-size: 12px; letter-spacing: 3px;
  }
</style>
</head>
<body>
<main class="sheet">

  <section class="card front" aria-label="Business card front">
    <svg class="card-art" viewBox="0 0 520 297" aria-hidden="true">
      <path class="band" d="M0 0 H262 C210 35 135 68 0 80 Z"/>
      <path class="swoosh" d="M0 92 C140 74 230 36 280 0 H298 C245 46 150 88 0 106 Z"/>
      <path class="swoosh" d="M0 116 C155 98 255 48 318 0 H324 C265 56 165 108 0 122 Z"/>
      <path class="band" d="M520 170 C400 178 290 215 215 297 H520 Z"/>
      <path class="swoosh" d="M520 150 C390 158 270 200 190 297 H172 C250 190 375 142 520 134 Z"/>
    </svg>
    <div class="person">
      <p class="person-name">Evan Carter</p>
      <p class="person-role">Owner / C.E.O</p>
    </div>
    <div class="brand"><span class="brand-dot"></span><span>Laurel Hollow Yoga</span></div>
    <ul class="contact">
      <li>Suite 14, Mill Ct, TN 37402
        <svg viewBox="0 0 24 24"><path d="M12 2a7 7 0 0 0-7 7c0 5 7 13 7 13s7-8 7-13a7 7 0 0 0-7-7zm0 9.5A2.5 2.5 0 1 1 12 6.5a2.5 2.5 0 0 1 0 5z"/></svg></li>
      <li>555-014-2291
        <svg viewBox="0 0 24 24"><path d="M6.6 10.8a15 15 0 0 0 6.6 6.6l2.2-2.2a1 1 0 0 1 1-.25 11.4 11.4 0 0 0 3.6.57 1 1 0 0 1 1 1V20a1 1 0 0 1-1 1A17 17 0 0 1 3 4a1 1 0 0 1 1-1h3.5a1 1 0 0 1 1 1c0 1.250.2 2.45.57 3.57a1 1 0 0 1-.25 1z"/></svg></li>
      <li>555-014-3378
        <svg viewBox="0 0 24 24"><path d="M6.6 10.8a15 15 0 0 0 6.6 6.6l2.2-2.2a1 1 0 0 1 1-.25 11.4 11.4 0 0 0 3.6.57 1 1 0 0 1 1 1V20a1 1 0 0 1-1 1A17 17 0 0 1 3 4a1 1 0 0 1 1-1h3.5a1 1 0 0 1 1 1c0 1.25.2 2.45.57 3.57a1 1 0 0 1-.25 1z"/></svg></li>
      <li>555-014-4602
        <svg viewBox="0 0 24 24"><path d="M6.6 10.8a15 15 0 0 0 6.6 6.6l2.2-2.2a1 1 0 0 1 1-.25 11.4 11.4 0 0 0 3.6.57 1 1 0 0 1 1 1V20a1 1 0 0 1-1 1A17 17 0 0 1 3 4a1 1 0 0 1 1-1h3.5a1 1 0 0 1 1 1c0 1.25.2 2.45.57 3.57a1 1 0 0 1-.25 1z"/></svg></li>
      <li>hello@laurelhollowyoga.com
        <svg viewBox="0 0 24 24"><path d="M3 5h18v14H3zm2 2v.5l7 4.5 7-4.5V7z"/></svg></li>
      <li>www.laurelhollowyoga.com
        <svg viewBox="0 0 24 24"><path d="M12 2a10 10 0 1 0 0 20 10 10 0 0 0 0-20zm0 2c1 1.3 1.8 3 2.2 5H9.8C10.2 7 11 5.3 12 4zM4.3 11h4.2c0 .7 0 1.3.1 2H4.3a8 8 0 0 1 0-2zm5.6 0h4.2a13 13 0 0 1 0 2H9.9a13 13 0 0 1 0-2zm5.6 0h4.2a8 8 0 0 1 0 2h-4.2c.1-.7.1-1.3 0-2zM9.8 15h4.4c-.4 2-1.2 3.7-2.2 5-1-1.3-1.8-3-2.2-5z"/></svg></li>
    </ul>
  </section>

  <section class="card back" aria-label="Business card back">
    <svg class="card-art" viewBox="0 0 520 297" aria-hidden="true">
      <path class="band" d="M0 80 C90 140 200 230 330 297 H0 Z"/>
      <path class="swoosh" d="M0 48 C110 110 250 235 390 297 H360 C230 240 100 125 0 64 Z"/>
      <path class="swoosh" d="M0 30 C130 90 270 220 420 297 H414 C270 228 120 100 0 36 Z"/>
    </svg>
    <div class="brand"><span class="brand-dot"></span><span>Laurel Hollow Yoga</span></div>
    <p class="web">www.laurelhollowyoga.com</p>
  </section>

</main>
</body>
</html>
```